E-commerce website for interior joinery product - Furnvale Trade

we want to create a E-commerce website to list our modular products.
other than E-commerce functions, we will also require membership logins and setting different price tiers for B2B customers (construction company and home building groups. for logos and our products etc please visit www.furnvale.co.nz
You can also get some ideas from https://brontecabinets.co.nz/ready-to-order/

Number of Pages Required

5+ page

Requirements
Must have
• on the product page, the customer can have the option to choose different colours and upgradable options.

```html
<!DOCTYPE html>
<html lang="en">
<head>
<meta charset="utf-8">
<title>Furnvale – Wardrobe &amp; door systems</title>
<link href="https://fonts.googleapis.com/css2?family=Catamaran:wght@500;600;700&family=Hind:wght@300;400;500;600&display=swap" rel="stylesheet">
<style>
:root{
  --teal:#5f8086;
  --teal-dark:#4d6a70;
  --frame:#2c3a3d;
  --ink:#2a2a2a;
  --muted:#8a8a8a;
  --line:#d9d9d9;
  --footer:#2d2d2d;
  --seal:#7f9196;
  --white:#ffffff;
}
*{box-sizing:border-box;margin:0;padding:0}
html,body{width:1200px;height:3318px;overflow:hidden;background:var(--white)}
body{position:relative;font-family:"Hind",sans-serif;color:var(--ink)}
.abs{position:absolute}
.btn{position:absolute;display:flex;align-items:center;justify-content:center;background:var(--teal);color:var(--white);font-size:13px;white-space:nowrap}

/* header */
.brand{left:45px;top:19px;display:flex;align-items:center;gap:12px}
.brand-mark{width:22px;height:22px;background:var(--teal);display:block}
.brand-name{font-family:"Hind",sans-serif;font-size:46px;font-weight:500;color:#6a6f72;line-height:1}
.brand-tag{font-size:12px;color:var(--teal);letter-spacing:1.3px;margin-top:2px}
.search{left:679px;top:17px;width:245px;height:30px;background:#f0f0f0;font-size:13px;font-style:italic;color:#aaa;padding:7px 10px}
.search svg{position:absolute;right:8px;top:7px}
.login{left:938px;top:17px;width:96px;height:30px}
.cart{left:1046px;top:17px;width:109px;height:30px;background:#a9a9a9}
.rule-top{left:372px;top:60px;width:783px;height:1px;background:var(--line)}
.nav{top:76px;font-size:13px;font-style:italic;color:var(--muted)}

/* hero */
.hero-panel{left:41px;top:117px;width:411px;height:602px;background:var(--teal);border:6px solid var(--frame);overflow:hidden}
.stripe{position:absolute;background:rgba(255,255,255,.12);height:14px;transform-origin:left}
.hero-title{position:absolute;left:0;width:100%;top:243px;text-align:center;font-family:"Catamaran",sans-serif;font-size:46px;font-weight:600;color:var(--white)}
.hero-sub{position:absolute;left:0;width:100%;top:306px;text-align:center;font-size:13px;color:var(--white)}
.hero-photo{left:466px;top:117px;width:689px;height:602px;border:6px solid var(--teal);background:linear-gradient(90deg,#e7e7e5 0%,#f2f2f0 40%,#dcdcda 100%)}
.hero-photo .floor{position:absolute;left:0;bottom:0;width:100%;height:160px;background:linear-gradient(180deg,#9a6c45,#6e4a2c)}
.dots{position:absolute;display:flex;gap:12px}
.dots i{width:9px;height:9px;background:var(--white);display:block}
.dots i.on{background:var(--teal)}

/* features */
.feature{position:absolute;top:769px;width:324px;height:99px;border:1px solid #cfcfcf;display:flex;align-items:center;gap:16px;padding:0 20px 0 30px}
.feature h3{font-family:"Catamaran",sans-serif;font-weight:600;font-size:16px;line-height:1.1}
.feature p{font-size:12px;font-style:italic;color:#666;line-height:1.35}

/* categories */
.category{position:absolute;top:933px;width:361px;height:359px;background:linear-gradient(135deg,#eeeeec,#d4d4d2)}
.category-label{position:absolute;left:63px;top:152px;width:235px;height:70px;background:var(--teal);color:var(--white);font-family:"Catamaran",sans-serif;font-size:22px;font-weight:600;display:flex;align-items:center;justify-content:center}

/* products */
.section-title{position:absolute;left:0;width:1200px;text-align:center;font-family:"Catamaran",sans-serif;font-weight:600;font-size:33px;color:var(--ink)}
.tabs{left:0;width:1200px;top:1398px;display:flex;justify-content:center;gap:20px;font-size:13px;color:var(--muted)}
.tabs span.on{color:var(--teal)}
.product{position:absolute;top:1440px;width:271px}
.product-photo{height:269px}
.product-name{position:absolute;top:292px;left:0;width:100%;text-align:center;font-family:"Catamaran",sans-serif;font-weight:600;font-size:16px}
.product-price{position:absolute;top:322px;left:0;width:100%;text-align:center;font-size:13px;color:#666}
.product .btn{top:348px;width:132px;height:34px}

/* testimonial */
.testimonial{left:38px;top:1957px;width:1114px;height:359px;background:linear-gradient(90deg,#5b4128 0%,#a17b56 30%,#8d8a80 55%,#a27e58 80%,#5d442d 100%);color:var(--white);text-align:center}
.testimonial h2{position:absolute;top:72px;width:100%;font-family:"Catamaran",sans-serif;font-weight:600;font-size:31px}
.testimonial p{position:absolute;top:132px;left:160px;width:794px;font-size:12px;line-height:1.3}
.testimonial .who{position:absolute;top:185px;width:100%;font-family:"Catamaran",sans-serif;font-weight:600;font-size:21px}

/* suppliers */
.supplier{position:absolute;width:219px;height:110px;border:1px solid #cfcfcf;display:flex;align-items:center;justify-content:center;gap:8px;font-family:"Hind",sans-serif;font-size:24px;font-weight:500;color:#444}
.supplier i{width:14px;height:14px;background:var(--teal);display:block}

/* footer */
.footer{left:33px;top:2935px;width:1118px;height:339px;background:var(--footer);color:var(--white)}
.footer h4{position:absolute;top:64px;font-family:"Catamaran",sans-serif;font-weight:600;font-size:16px}
.footer .item{position:absolute;font-size:13px;color:#e6e6e6;display:flex;align-items:center;gap:10px;white-space:nowrap}
.footer .item b{width:4px;height:4px;background:#888;display:block}
.field{position:absolute;border:1px solid #bbb;font-size:12px;font-style:italic;padding:7px 10px;color:#ddd}
.seal{position:absolute;left:950px;top:42px;width:128px;height:128px;border-radius:50%;background:var(--seal)}
.social{position:absolute;top:206px;display:flex;gap:10px;left:923px}
.social i{width:25px;height:25px;border:1.5px solid #aaa;border-radius:50%;display:block}
.footer-rule{position:absolute;left:0;top:270px;width:100%;height:1px;background:#555}
.copyright{position:absolute;left:43px;top:298px;font-size:13px}
.pay{position:absolute;top:292px;left:892px;display:flex;gap:4px}
.pay span{height:26px;padding:0 5px;background:#f2f2f2;color:#222;font-size:11px;font-weight:600;display:flex;align-items:center}
</style>
</head>
<body>

<!-- header -->
<div class="abs brand">
  <span class="brand-mark"></span>
  <div>
    <div class="brand-name">Furnvale</div>
    <div class="brand-tag">Wardrobe &amp; door systems</div>
  </div>
</div>
<div class="abs search">Search Here
  <svg width="16" height="16" viewBox="0 0 16 16" fill="none" stroke="#999" stroke-width="1.4"><circle cx="7" cy="7" r="5"/><path d="M11 11l4 4"/></svg>
</div>
<div class="btn login">
  <svg width="14" height="14" viewBox="0 0 14 14" fill="none" stroke="#fff" stroke-width="1.3" style="margin-right:6px"><circle cx="7" cy="4.5" r="3"/><path d="M1.5 13c.5-3 2.7-4.5 5.5-4.5s5 1.5 5.5 4.5"/></svg>Login
</div>
<div class="btn cart">
  <svg width="15" height="14" viewBox="0 0 15 14" fill="none" stroke="#fff" stroke-width="1.3" style="margin-right:6px"><path d="M1 1h2l2 8h8l1.5-6H4"/><circle cx="6" cy="12" r="1"/><circle cx="12" cy="12" r="1"/></svg>My Cart (0)
</div>
<div class="abs rule-top"></div>
<div class="abs nav" style="left:903px">Home</div>
<div class="abs nav" style="left:960px">Products</div>
<div class="abs nav" style="left:1033px">Gallery</div>
<div class="abs nav" style="left:1094px">Contact us</div>

<!-- hero -->
<section class="abs hero-panel">
  <span class="stripe" style="left:-20px;top:165px;width:480px;transform:rotate(-20deg)"></span>
  <span class="stripe" style="left:-20px;top:205px;width:480px;transform:rotate(-20deg);height:6px"></span>
  <span class="stripe" style="left:-20px;top:540px;width:220px;transform:rotate(-20deg)"></span>
  <h1 class="hero-title">Wardrobe Doors</h1>
  <p class="hero-sub">Design to Decorate kiwi Homes</p>
  <span class="btn" style="left:68px;top:335px;width:117px;height:34px;background:#fff;color:#999">View Products</span>
  <span class="btn" style="left:195px;top:335px;width:131px;height:34px;background:#9aa9ab">Visit Showrooms</span>
</section>
<div class="abs hero-photo" role="img" aria-label="Bright bedroom with a white sliding-door wardrobe, bed and timber floor">
  <div class="floor"></div>
  <div class="dots" style="right:30px;bottom:22px"><i class="on"></i><i></i><i></i></div>
</div>

<!-- features -->
<div class="feature" style="left:94px">
  <svg width="52" height="52" viewBox="0 0 52 52" fill="none" stroke="#555" stroke-width="1.6"><rect x="4" y="18" width="40" height="28" rx="2"/><path d="M14 18l16-14 10 8M30 30h14v8H30z"/></svg>
  <div><h3>Payment Option</h3><p>Cash • Internet Banking • Cheque</p></div>
</div>
<div class="feature" style="left:436px">
  <svg width="60" height="50" viewBox="0 0 60 50" fill="none" stroke="#555" stroke-width="1.6"><rect x="4" y="8" width="34" height="28"/><path d="M38 16h10l8 10v10H38zM14 22l5 5 9-9"/><circle cx="14" cy="40" r="4"/><circle cx="46" cy="40" r="4"/></svg>
  <div><h3>Delivery Options</h3><p>Flat pack or Assembled (Cost of delivery will be given in a formal quotation).</p></div>
</div>
<div class="feature" style="left:778px">
  <svg width="56" height="52" viewBox="0 0 56 52" fill="none" stroke="#555" stroke-width="1.6"><path d="M46 18a20 20 0 0 0-38 4M10 34a20 20 0 0 0 38-4M4 18l4 5 5-4M52 34l-4-5-5 4M33 19h-7a3.5 3.5 0 0 0 0 7h4a3.5 3.5 0 0 1 0 7h-8M28 15v22"/></svg>
  <div><h3>Money Back Gurantee</h3><p>Lorem Ipsum is simply dummy text of the printing and typesetting.</p></div>
</div>

<!-- categories -->
<div class="category" style="left:41px" role="img" aria-label="Frosted sliding wardrobe doors in a white room">
  <span class="category-label">Sliding Doors</span>
</div>
<div class="category" style="left:418px" role="img" aria-label="Open walk-in wardrobe shelving with hangers">
  <span class="category-label">Wardrobe System</span>
</div>
<div class="category" style="left:796px" role="img" aria-label="Bedroom with built-in storage shelves">
  <span class="category-label">Storage Space</span>
</div>

<!-- feature products -->
<h2 class="section-title" style="top:1328px">Feature Products</h2>
<div class="abs tabs"><span class="on">ALL</span><span>Latest</span><span>Best Seller</span><span>Sale</span></div>

<div class="product" style="left:38px">
  <div class="product-photo" role="img" aria-label="Glass room divider doors in a study" style="background:linear-gradient(160deg,#dedad4,#b89a7c)"></div>
  <div class="product-name">Room Divider</div><div class="product-price">$599.00</div>
  <span class="btn" style="left:65px">Add To Cart</span>
</div>
<div class="product" style="left:321px">
  <div class="product-photo" role="img" aria-label="White hinged wardrobe doors" style="background:linear-gradient(160deg,#f1f1ef,#d8d8d5)"></div>
  <div class="product-name">Hinge Doors</div><div class="product-price">$599.00</div>
  <span class="btn" style="left:62px">Add To Cart</span>
</div>
<div class="product" style="left:603px">
  <div class="product-photo" role="img" aria-label="Basic wardrobe with shelves and drawers" style="background:linear-gradient(160deg,#d9d2c8,#a89b8c)"></div>
  <div class="product-name">Basic Wardrobe</div><div class="product-price">$599.00</div>
  <span class="btn" style="left:75px">Add To Cart</span>
</div>
<div class="product" style="left:885px">
  <div class="product-photo" role="img" aria-label="Linen cupboard with towels and baskets" style="background:linear-gradient(160deg,#efece8,#b48e6a)"></div>
  <div class="product-name">Linen Cubboard</div><div class="product-price">$599.00</div>
  <span class="btn" style="left:78px">Add To Cart</span>
</div>

<span class="btn" style="left:535px;top:1883px;width:131px;height:34px">Browse More</span>

<!-- testimonial -->
<section class="abs testimonial" role="img" aria-label="Blurred showroom interior behind a client testimonial">
  <h2>Our Clients Say`s</h2>
  <p>Lorem Ipsum is simply dummy text of the printing and typesetting industry. Lorem Ipsum has been the industry's standard dummy text ever since the 1500s, when an unknown printer took a galley of type and scrambled it to make a type specimen book</p>
  <div class="who">Mark Tane</div>
  <svg class="abs" style="left:518px;top:226px" width="78" height="14" viewBox="0 0 78 14" fill="#f2c230">
    <path id="st" d="M7 0l2 5h5l-4 3 1.6 5L7 10l-4.6 3L4 8 0 5h5z"/>
    <use href="#st" x="16"/><use href="#st" x="32"/><use href="#st" x="48"/><use href="#st" x="64"/>
  </svg>
  <div class="dots" style="left:532px;top:295px"><i class="on"></i><i></i><i></i></div>
</section>

<!-- suppliers -->
<h2 class="section-title" style="top:2372px">Proudly Supplier</h2>
<div class="supplier" style="left:131px;top:2466px"><i></i>Bramwell</div>
<div class="supplier" style="left:369px;top:2466px">Corelane Panels</div>
<div class="supplier" style="left:607px;top:2466px">Ashgrove</div>
<div class="supplier" style="left:844px;top:2466px">Lumetra</div>
<div class="supplier" style="left:131px;top:2601px">Veneris</div>
<div class="supplier" style="left:369px;top:2601px">Quarrystone</div>
<div class="supplier" style="left:607px;top:2601px">Kestrel</div>
<div class="supplier" style="left:844px;top:2601px">Halvorn</div>
<div class="supplier" style="left:254px;top:2731px"><i></i>Tessin</div>
<div class="supplier" style="left:491px;top:2731px">Marlowe</div>
<div class="supplier" style="left:730px;top:2731px">Rinaldo Vetti</div>

<!-- footer -->
<footer class="abs footer">
  <h4 style="left:43px">Quick Links</h4>
  <div class="item" style="left:43px;top:95px"><b></b>Home</div>
  <div class="item" style="left:43px;top:135px"><b></b>Products</div>
  <div class="item" style="left:43px;top:176px"><b></b>Gallery</div>
  <div class="item" style="left:43px;top:217px"><b></b>Buyer's Guide</div>

  <h4 style="left:226px">Products</h4>
  <div class="item" style="left:226px;top:95px"><b></b>Doors</div>
  <div class="item" style="left:226px;top:135px"><b></b>Wardrobe System</div>
  <div class="item" style="left:226px;top:176px"><b></b>Storage Space</div>
  <div class="item" style="left:226px;top:217px"><b></b>Accessories</div>

  <h4 style="left:403px">Branches</h4>
  <div class="item" style="left:428px;top:95px">Auckland Showroom</div>
  <div class="item" style="left:406px;top:135px"><svg width="14" height="14" viewBox="0 0 14 14" fill="#9ab"><path d="M3 1l2.5 3-1.5 2a8 8 0 0 0 4 4l2-1.5 3 2.5-1.5 2C6 13 1 8 1 2.5z"/></svg>09 555 0142</div>
  <div class="item" style="left:428px;top:176px">Hamilton Showroom</div>
  <div class="item" style="left:406px;top:217px"><svg width="14" height="14" viewBox="0 0 14 14" fill="#9ab"><path d="M3 1l2.5 3-1.5 2a8 8 0 0 0 4 4l2-1.5 3 2.5-1.5 2C6 13 1 8 1 2.5z"/></svg>07 555 0187</div>

  <h4 style="left:605px">Contact us</h4>
  <div class="field" style="left:605px;top:100px;width:140px;height:32px">Full Name</div>
  <div class="field" style="left:748px;top:100px;width:141px;height:32px">Email</div>
  <div class="field" style="left:605px;top:138px;width:284px;height:50px">Message</div>
  <span class="btn" style="left:605px;top:197px;width:130px;height:33px">Submit Now</span>

  <div class="seal" role="img" aria-label="Guarantee badge"></div>
  <div class="social"><i></i><i></i><i></i><i></i><i></i></div>

  <div class="footer-rule"></div>
  <div class="copyright">Copyright © 2019 Furnvale. All Right Reserved</div>
  <div class="pay"><span>Cardex</span><span>Tapwallet</span><span>Globepay</span><span>Norcard</span></div>
</footer>

</body>
</html>
```